Business Card Design for Photographer

Updating business card design. Must use included logo. We're a luxury wedding photography business. Elegancy, luxury, consistency are messages we wish to convey.

Visit our website at www.colbyvarnway.com to familiarize yourself more with our brand design currently (fonts, colors etc.). This is what we want to maintain.

Target Market(s)

Luxury Brides and Grooms

Industry/Entity Type

Wedding

Contact Information for Business Card

Current logo (attached to brief)
Name: Colby Varnway
Phone: 5208813047
website/blog
Email

Requirements
Must have
• Current logo (attached to brief)
• Name: Colby Varnway
• Phone: 5208813047
• website/blog
• Email
• Social username
Should not have
• bright colors, fonts that don't suit our brand (visit www.colbyvarnway.com)

```html
<!DOCTYPE html>
<html lang="en">
<head>
<meta charset="utf-8">
<title>Colby Varnway – Business Cards</title>
<link rel="stylesheet" href="https://fonts.googleapis.com/css2?family=Josefin+Sans:wght@300;400&family=Lato:wght@300;400&display=swap">
<style>
  :root {
    --page: #ffffff;
    --card: #f6f7f9;
    --band: #dfe0e2;
    --tile: #eff0f3;
    --label-bg: #eeeff2;
    --ink: #6b6c6f;
    --ink-dark: #5f6064;
    --shadow: rgba(0, 0, 0, 0.28);
  }
  * { margin: 0; padding: 0; box-sizing: border-box; }
  html, body {
    width: 1200px;
    height: 900px;
    overflow: hidden;
    background: var(--page);
  }
  .canvas {
    position: relative;
    width: 1200px;
    height: 900px;
  }
  .card {
    position: absolute;
    background: var(--card);
    box-shadow: 2px 3px 5px var(--shadow);
    overflow: hidden;
  }
  .card--front { left: 37px; top: 20px; width: 683px; height: 417px; }
  .card--back  { left: 465px; top: 458px; width: 683px; height: 414px; }

  .band { position: absolute; background: var(--band); }

  .monogram {
    position: absolute;
    width: 96px;
    height: 76px;
    background: var(--tile);
    display: flex;
    align-items: center;
    justify-content: center;
    text-align: center;
    font-family: "Josefin Sans", sans-serif;
    font-weight: 400;
    font-size: 14px;
    line-height: 1.25;
    letter-spacing: 0.08em;
    text-transform: uppercase;
    color: var(--ink-dark);
  }

  .holder-name {
    position: absolute;
    height: 30px;
    padding: 0 6px;
    background: var(--label-bg);
    font-family: "Josefin Sans", sans-serif;
    font-weight: 300;
    font-size: 21px;
    line-height: 34px;
    letter-spacing: 0.2em;
    text-transform: uppercase;
    color: var(--ink);
    white-space: nowrap;
  }
  .holder-name .cap { font-size: 25px; }

  .contact-list {
    position: absolute;
    list-style: none;
    font-family: "Lato", sans-serif;
    font-weight: 400;
    font-size: 17px;
    color: var(--ink);
  }
  .contact-list li {
    display: flex;
    align-items: center;
    height: 32px;
  }
  .contact-icon {
    width: 26px;
    height: 26px;
    margin-right: 11px;
    flex: none;
    display: flex;
    align-items: center;
    justify-content: center;
  }
  .contact-icon svg { display: block; }
  .contact-icon--at {
    font-family: "Lato", sans-serif;
    font-style: italic;
    font-weight: 400;
    font-size: 20px;
    color: var(--ink-dark);
  }
</style>
</head>
<body>
<main class="canvas">

  <!-- Front card -->
  <section class="card card--front" aria-label="Business card, front layout">
    <div class="band" style="left:0; top:43px; width:49px; height:62px;"></div>
    <div class="monogram" style="left:69px; top:35px;">Colby<br>Varnway</div>
    <div class="band" style="left:185px; top:43px; width:498px; height:62px;"></div>

    <p class="holder-name" style="left:82px; top:208px;"><span class="cap">C</span>olby <span class="cap">V</span>arnway</p>

    <ul class="contact-list" style="left:92px; top:249px;">
      <li>
        <span class="contact-icon">
          <svg width="24" height="26" viewBox="0 0 24 26" aria-hidden="true"><rect x="3" y="1.5" width="13" height="22" rx="3" transform="rotate(-14 10 13)" fill="none" stroke="#5f6064" stroke-width="1.6"/><rect x="10" y="17" width="6" height="3" rx="1" transform="rotate(-14 10 13)" fill="#5f6064"/></svg>
        </span>5208813047
      </li>
      <li><span class="contact-icon contact-icon--at">@</span>website/blog</li>
      <li>
        <span class="contact-icon">
          <svg width="22" height="16" viewBox="0 0 22 16" aria-hidden="true"><rect x="1" y="1" width="20" height="14" fill="none" stroke="#5f6064" stroke-width="1.6"/><path d="M1 1 L11 9 L21 1 M1 15 L8 7 M21 15 L14 7" fill="none" stroke="#5f6064" stroke-width="1.4"/></svg>
        </span>Email
      </li>
      <li>
        <span class="contact-icon">
          <svg width="20" height="20" viewBox="0 0 20 20" aria-hidden="true"><rect x="1" y="1" width="18" height="18" rx="4" fill="#5f6064"/></svg>
        </span>Social username
      </li>
    </ul>
  </section>

  <!-- Back card -->
  <section class="card card--back" aria-label="Business card, centred layout">
    <div class="band" style="left:0; top:190px; width:146px; height:190px;"></div>
    <div class="band" style="left:539px; top:190px; width:144px; height:190px;"></div>

    <div class="monogram" style="left:197px; top:79px;">Colby<br>Varnway</div>

    <p class="holder-name" style="left:205px; top:174px;"><span class="cap">C</span>olby <span class="cap">V</span>arnway</p>

    <ul class="contact-list" style="left:211px; top:215px;">
      <li>
        <span class="contact-icon">
          <svg width="24" height="26" viewBox="0 0 24 26" aria-hidden="true"><rect x="3" y="1.5" width="13" height="22" rx="3" transform="rotate(-14 10 13)" fill="none" stroke="#5f6064" stroke-width="1.6"/><rect x="10" y="17" width="6" height="3" rx="1" transform="rotate(-14 10 13)" fill="#5f6064"/></svg>
        </span>5208813047
      </li>
      <li><span class="contact-icon contact-icon--at">@</span>website/blog</li>
      <li>
        <span class="contact-icon">
          <svg width="22" height="16" viewBox="0 0 22 16" aria-hidden="true"><rect x="1" y="1" width="20" height="14" fill="none" stroke="#5f6064" stroke-width="1.6"/><path d="M1 1 L11 9 L21 1 M1 15 L8 7 M21 15 L14 7" fill="none" stroke="#5f6064" stroke-width="1.4"/></svg>
        </span>Email
      </li>
      <li>
        <span class="contact-icon">
          <svg width="20" height="20" viewBox="0 0 20 20" aria-hidden="true"><rect x="1" y="1" width="18" height="18" rx="4" fill="#5f6064"/></svg>
        </span>Social username
      </li>
    </ul>
  </section>

</main>
</body>
</html>
```